Startup internet service provider needs a good facebook ad

Looking for a catchy facebook ad to launch our internet service in Parker, Colorado. Short video or slideshow preferred, still pictures are okay.

https://www.facebook.com/BrimfoxNetworks

www.brimfox-networks.example

Target Market(s)

Parker Colorado

Colors
add136
0255a3

```html
<!DOCTYPE html>
<html lang="en">
<head>
<meta charset="UTF-8">
<title>Brimfox Networks – Fast and Reliable Internet</title>
<link rel="stylesheet" href="https://fonts.googleapis.com/css2?family=Montserrat:wght@400;500;700;800&display=swap">
<style>
  :root {
    --navy: #0b1a35;
    --lime: #add136;
    --brand-blue: #2563a8;
    --text-light: #e4e8ef;
    --city-gold: #8a6a2a;
    --city-amber: #5a4520;
    --city-blue: #2a5d9a;
    --city-glow: #4f86c8;
    --city-dark: #141c28;
  }
  * { margin: 0; padding: 0; box-sizing: border-box; }
  html, body {
    width: 1200px;
    height: 1200px;
    overflow: hidden;
    background: var(--navy);
  }
  .ad {
    position: relative;
    width: 1200px;
    height: 1200px;
    background: var(--navy);
    font-family: "Montserrat", sans-serif;
    overflow: hidden;
  }
  .brand {
    position: absolute;
    left: 72px;
    top: 67px;
    display: flex;
    align-items: center;
    gap: 20px;
    z-index: 2;
  }
  .brand-dot {
    width: 80px;
    height: 80px;
    border-radius: 50%;
    background: var(--lime);
  }
  .brand-name {
    font-weight: 500;
    font-size: 40px;
    color: var(--brand-blue);
    letter-spacing: 0.2px;
  }
  .headline {
    position: absolute;
    left: 72px;
    top: 229px;
    font-weight: 700;
    font-size: 43px;
    line-height: 48px;
    color: var(--lime);
    text-transform: uppercase;
    letter-spacing: 0;
    z-index: 2;
  }
  .benefits {
    position: absolute;
    left: 72px;
    top: 398px;
    list-style: none;
    font-weight: 400;
    font-size: 22.5px;
    line-height: 39px;
    color: var(--text-light);
    z-index: 2;
  }
  .benefits li::before { content: "– "; }
  .city-scene {
    position: absolute;
    left: 0;
    top: 700px;
    width: 1200px;
    height: 500px;
    z-index: 1;
    background:
      linear-gradient(to bottom, var(--navy) 0%, rgba(11,26,53,0) 22%),
      radial-gradient(ellipse 260px 160px at 18% 78%, var(--city-gold) 0%, rgba(138,106,42,0) 100%),
      radial-gradient(ellipse 300px 140px at 62% 92%, var(--city-gold) 0%, rgba(138,106,42,0) 100%),
      radial-gradient(ellipse 220px 120px at 88% 58%, var(--city-amber) 0%, rgba(90,69,32,0) 100%),
      radial-gradient(ellipse 360px 200px at 45% 55%, var(--city-glow) 0%, rgba(79,134,200,0) 100%),
      radial-gradient(ellipse 300px 180px at 80% 80%, var(--city-blue) 0%, rgba(42,93,154,0) 100%),
      radial-gradient(ellipse 260px 150px at 8% 40%, var(--city-blue) 0%, rgba(42,93,154,0) 100%),
      linear-gradient(to bottom, #13243f 0%, var(--city-dark) 55%, #1e1f24 100%);
  }
</style>
</head>
<body>
  <main class="ad">
    <header class="brand">
      <span class="brand-dot"></span>
      <span class="brand-name">Brimfox Networks</span>
    </header>

    <h1 class="headline">Fast and reliable&nbsp; internet service<br>designed and catered to meet<br>your needs</h1>

    <ul class="benefits">
      <li>Fast and reliable internet service</li>
      <li>Real customer support</li>
      <li>Less buffering while streaming</li>
      <li>Fast web browsing</li>
      <li>Gaming without the lag</li>
      <li>Wall to wall WiFi coverage</li>
      <li>No introductory charges, one constant rate</li>
      <li>Simple and easy to read bills</li>
    </ul>

    <div class="city-scene" role="img" aria-label="Aerial night view of a lit city with glowing network connection arcs linking points across the skyline"></div>
  </main>
</body>
</html>
```